Red Fern Media Outdoor Advertising Corporate Stationery Design

We need a full corporate stationary design for our company Red Fern Media. We setup and lease billboards, building wraps, trailer ads and construction hoardings.

We need to establish our branding and our newly created logo. All our brand identity should point towards our values, vision and mission.

We are open to fresh new ideas for our stationary design as long as it ultimately reflects the brand & logo.

Corporate Stationary List:
1. Business Card Design
2. Letterhead Design
3. Email Signature Design
4. “Advertise Here” Design (for placement on empty billboards, etc)

All designs must include our logo and be kept simple, modern, friendly and effective.

All designs should please be provided in Illustrator, Photoshop and InDesign file formats.

More details are attached in Word.

Hey

The project has been guaranteed. We like what has been submitted so far but we''d like to see a few concepts for the "Advertise Here" design for open billboards please.

Thanks!

Target Market(s)

Male and female, corporates, business owners, media buying agencies, government & all age groups.

Industry/Entity Type

Construction

Requirements
Must have
• All designs must incorporate our colours: Pantone 319C, 320C, 321C & Hexachrome Black C.

1.Business Card Design
a. Logo
b. Name
c. Mobile
d. Landline
e. Website
f. Facebook
g. Twitter
2. Letterhead Design
a. Logo
b. Mobile
c. Landline
d. Website
e. CC reg number
f. BEE level 4 contributor
g. PRAVU member
h. Postal Address
3. Email Signature Design
a. Logo
b. Name
c. Mobile
d. Landline
e. BEE level 4 contributor
f. PRAVU member
g. Website
h. Facebook
i. Twitter
4. “Advertise Here” Design (for placement on empty billboards, etc) Majority ratio of 2:1 (eg 6m wide by 3m high) - Please use 2 attached photos.
a. Logo .co.za
b. Contact Nadia
c. Mobile
Nice to have
• Come up with a cool slogan / tagline for Business Cards, “Advertise Here” Design

```html
<!DOCTYPE html>
<html lang="en">
<head>
<meta charset="utf-8">
<title>Red Fern Media – Business Card</title>
<link href="https://fonts.googleapis.com/css2?family=Arimo:wght@400;700&display=swap" rel="stylesheet">
<style>
  :root {
    --teal-light: #7fcdd1;
    --teal: #3aa9b2;
    --teal-deep: #137f8a;
    --ink: #111213;
    --card-black: #050505;
    --paper: #ffffff;
    --stage: #d9dadb;
    --muted: #8a8a8a;
  }
  * { margin: 0; padding: 0; box-sizing: border-box; }
  html, body {
    width: 1200px; height: 880px; overflow: hidden;
    background: var(--stage);
    font-family: "Arimo", Arial, sans-serif;
  }
  .canvas {
    width: 1200px; height: 880px;
    display: flex; align-items: center; justify-content: center; gap: 60px;
  }
  .card {
    position: relative;
    width: 525px; height: 300px;
    box-shadow: 0 10px 30px rgba(0,0,0,.25);
    overflow: hidden;
  }

  /* Front (black) */
  .card--front { background: var(--card-black); }
  .card--front .rule {
    position: absolute; left: 0; right: 0; top: 118px;
    height: 1px; background: var(--teal);
  }
  .card--front .brand-mark {
    position: absolute; left: 100px; top: 80px;
    width: 76px; height: 76px; background: var(--teal);
  }
  .card--front .brand-name {
    position: absolute; left: 78px; top: 166px;
    font-weight: 700; font-size: 38px; line-height: 44px; letter-spacing: -0.5px;
    color: var(--teal-light); white-space: nowrap;
  }
  .card--front .web {
    position: absolute; right: 28px; top: 111px;
    background: var(--card-black); padding: 0 8px;
    font-size: 10px; line-height: 14px; letter-spacing: 3px; color: var(--muted);
    white-space: nowrap;
  }

  /* Back (white) */
  .card--back { background: var(--paper); }
  .card--back .brand {
    position: absolute; left: 40px; top: 34px;
    display: flex; align-items: center; gap: 9px;
  }
  .card--back .brand-mark { width: 22px; height: 22px; background: var(--teal); }
  .card--back .brand-name {
    font-weight: 700; font-size: 22px; letter-spacing: -0.3px; color: var(--teal-deep);
  }
  .card--back .rule {
    position: absolute; left: 0; right: 0; top: 196px;
    height: 1px; background: var(--teal-light);
  }
  .contact-list {
    position: absolute; left: 40px; top: 88px;
    list-style: none;
  }
  .contact-list li {
    display: flex; align-items: center; gap: 9px;
    font-size: 12.5px; line-height: 20px; color: var(--ink);
  }
  .contact-list li.phone { font-size: 14px; }
  .contact-list svg { width: 12px; height: 12px; flex: none; fill: var(--teal); }
  .person {
    position: absolute; right: 40px; top: 170px; text-align: right;
  }
  .person-name { font-size: 19px; color: var(--ink); line-height: 24px; }
  .person-role { font-size: 12px; color: var(--teal); margin-top: 6px; }
</style>
</head>
<body>
<main class="canvas">

  <section class="card card--front" aria-label="Business card front">
    <div class="rule"></div>
    <span class="brand-mark"></span>
    <span class="brand-name">Red Fern Media</span>
    <span class="web">www.redfernmedia.com</span>
  </section>

  <section class="card card--back" aria-label="Business card back">
    <div class="brand">
      <span class="brand-mark"></span>
      <span class="brand-name">Red Fern Media</span>
    </div>

    <ul class="contact-list">
      <li class="address">
        <svg viewBox="0 0 12 12" aria-hidden="true"><path d="M6 1 1 5.5h1.5V11h3V8h1v3h3V5.5H11z"/></svg>
        2210 Harbour Crest Road, Lakeview, FL 34210
      </li>
      <li class="phone">
        <svg viewBox="0 0 12 12" aria-hidden="true"><rect x="3" y="0.5" width="6" height="11" rx="1"/><rect x="4" y="2" width="4" height="6.5" fill="#fff"/></svg>
        410 555 2368
      </li>
      <li class="email">
        <svg viewBox="0 0 12 12" aria-hidden="true"><rect x="0.5" y="2.5" width="11" height="7" rx="1"/><path d="M1 3l5 3.5L11 3" stroke="#fff" stroke-width="1" fill="none"/></svg>
        hello@redfernmedia.com
      </li>
      <li class="web">
        <svg viewBox="0 0 12 12" aria-hidden="true"><circle cx="6" cy="6" r="5.5"/><path d="M0.5 6h11M6 0.5c-2.5 3-2.5 8 0 11M6 0.5c2.5 3 2.5 8 0 11" stroke="#fff" stroke-width=".8" fill="none"/></svg>
        www.redfernmedia.com
      </li>
    </ul>

    <div class="rule"></div>
    <div class="person">
      <p class="person-name">Sam Carter</p>
      <p class="person-role">Manager</p>
    </div>
  </section>

</main>
</body>
</html>
```